Pull Up Banners

Would like to have these pull up banner designs changed to a new modern theme. I have running a sales booth and want to re-design the banner designs. I have uploaded old banner design, I need phone number and website added onto bottom. Happy to consider images to attract people attention to increase sales and spark people interest walking past.

```html
<!DOCTYPE html>
<html lang="en">
<head>
<meta charset="utf-8">
<title>Brightline – Cloud Phone System &amp; Internet Pull Up Banner</title>
<link href="https://fonts.googleapis.com/css2?family=Montserrat:wght@400;600;700;800&display=swap" rel="stylesheet">
<style>
  :root {
    --page-bg: #e4e4e4;
    --banner-white: #ffffff;
    --orange-deep: #e0602a;
    --orange-mid: #e2701c;
    --orange-warm: #ea8a1a;
    --night: #15140f;
    --olive: #3d4526;
    --ink: #111111;
    --white: #ffffff;
  }
  * { box-sizing: border-box; margin: 0; padding: 0; }
  html, body { width: 1141px; height: 1200px; overflow: hidden; }
  body {
    background: var(--page-bg);
    font-family: "Montserrat", Arial, sans-serif;
    position: relative;
  }
  .banner {
    position: absolute;
    left: 337px; top: 20px;
    width: 466px; height: 1160px;
    background: var(--banner-white);
    overflow: hidden;
  }
  .banner__field {
    position: absolute; inset: 0;
    width: 466px; height: 1160px;
  }
  .banner__photo {
    position: absolute; left: 0; top: 0;
    width: 466px; height: 480px;
    background:
      radial-gradient(ellipse 70% 60% at 95% 20%, rgba(61,69,38,0.95), rgba(61,69,38,0) 70%),
      radial-gradient(ellipse 60% 45% at 85% 62%, rgba(21,20,15,0.95), rgba(21,20,15,0) 75%),
      linear-gradient(100deg, rgba(224,96,42,0.95) 0%, rgba(196,84,30,0.85) 35%, rgba(30,28,20,0.9) 70%, rgba(21,20,15,0.9) 100%);
    -webkit-mask-image: linear-gradient(180deg, #000 70%, transparent 100%);
            mask-image: linear-gradient(180deg, #000 70%, transparent 100%);
  }
  .brand {
    position: absolute; left: 40px; top: 40px;
    display: flex; align-items: center; gap: 14px;
  }
  .brand__dot {
    width: 40px; height: 40px; border-radius: 50%;
    background: var(--white);
  }
  .brand__text { display: flex; flex-direction: column; }
  .brand__name {
    font-weight: 600; font-size: 30px; letter-spacing: 3px;
    color: var(--white); line-height: 1;
  }
  .brand__tagline {
    margin-top: 5px;
    font-size: 7px; letter-spacing: 1.6px; color: var(--white);
  }
  .headline {
    position: absolute; left: 41px; top: 320px;
    font-weight: 800; font-size: 37px; line-height: 47px;
    color: var(--white); letter-spacing: 0.3px;
  }
  .headline__rule {
    position: absolute; left: 41px; top: 494px;
    width: 51px; height: 4px; background: var(--white);
  }
  .service {
    position: absolute; width: 180px; text-align: center;
    color: var(--white); font-size: 16.5px; line-height: 21px;
    white-space: nowrap;
  }
  .service__icon {
    display: block; width: 78px; height: 78px; margin: 0 auto 15px;
  }
  .contact {
    position: absolute; left: 0; width: 466px; text-align: center;
    color: var(--ink); font-weight: 700;
  }
  .contact--phone { top: 1054px; font-size: 30px; }
  .contact--web { top: 1093px; font-size: 25.5px; }
</style>
</head>
<body>
  <main class="banner">
    <svg class="banner__field" viewBox="0 0 466 1160" aria-hidden="true">
      <defs>
        <linearGradient id="orangeField" x1="0" y1="0" x2="1" y2="1">
          <stop offset="0" stop-color="#e0602a"/>
          <stop offset="0.55" stop-color="#e2701c"/>
          <stop offset="1" stop-color="#ea8a1a"/>
        </linearGradient>
      </defs>
      <path d="M0 0 H466 V990 Q466 1036 414 1036 C280 1030 90 985 0 868 Z" fill="url(#orangeField)"/>
    </svg>

    <div class="banner__photo" role="img" aria-label="Photo of a finger tapping a glowing tablet screen with floating cloud and wifi symbols"></div>

    <header class="brand">
      <span class="brand__dot"></span>
      <div class="brand__text">
        <span class="brand__name">BRIGHTLINE</span>
        <span class="brand__tagline">SMART TECH SUPPORT FOR EVERY BUSINESS</span>
      </div>
    </header>

    <h1 class="headline">CLOUD PHONE<br>SYSTEM &amp;<br>INTERNET</h1>
    <div class="headline__rule"></div>

    <section class="service" style="left:11px; top:538px;">
      <svg class="service__icon" viewBox="0 0 78 78" aria-hidden="true">
        <circle cx="39" cy="39" r="38" fill="none" stroke="#111" stroke-width="1.6"/>
        <path d="M25 22 l7 -2 5 10 -4 4 c2 5 5 8 10 10 l4 -4 10 5 -2 7 c-16 2 -32 -14 -30 -30z" fill="#111"/>
        <path d="M41 28 a9 9 0 0 1 9 9 M41 22 a15 15 0 0 1 15 15 M41 16 a21 21 0 0 1 21 21" fill="none" stroke="#111" stroke-width="2.5" stroke-linecap="round"/>
      </svg>
      VoIP &amp; Phone<br>Systems
    </section>

    <section class="service" style="left:176px; top:538px;">
      <svg class="service__icon" viewBox="0 0 78 78" aria-hidden="true">
        <circle cx="39" cy="39" r="38" fill="none" stroke="#111" stroke-width="1.6"/>
        <rect x="15" y="21" width="48" height="32" rx="4" fill="#111"/>
        <path d="M26 52 l0 10 9 -10z" fill="#111"/>
        <path d="M22 30 h34 M22 37 h34 M22 44 h34" stroke="#e2701c" stroke-width="2"/>
      </svg>
      SMS Gateway
    </section>

    <section class="service" style="left:11px; top:718px;">
      <svg class="service__icon" viewBox="0 0 78 78" aria-hidden="true">
        <circle cx="39" cy="39" r="38" fill="none" stroke="#111" stroke-width="1.6"/>
        <circle cx="39" cy="27" r="7" fill="#111"/>
        <circle cx="23" cy="33" r="5" fill="#111"/>
        <circle cx="55" cy="33" r="5" fill="#111"/>
        <path d="M27 56 c0 -15 24 -15 24 0z" fill="#111"/>
        <path d="M13 55 c0 -12 14 -13 17 -6 l-2 6z M65 55 c0 -12 -14 -13 -17 -6 l2 6z" fill="#111"/>
      </svg>
      Team Chat<br>Calling
    </section>

    <section class="service" style="left:176px; top:718px;">
      <svg class="service__icon" viewBox="0 0 78 78" aria-hidden="true">
        <circle cx="39" cy="39" r="38" fill="none" stroke="#111" stroke-width="1.6"/>
        <path d="M14 33 a36 36 0 0 1 50 0 M21 41 a26 26 0 0 1 36 0 M28 48 a15 15 0 0 1 22 0" fill="none" stroke="#111" stroke-width="5" stroke-linecap="round"/>
        <circle cx="39" cy="57" r="4.5" fill="#111"/>
      </svg>
      Broadband, Fibre &amp;<br>4G Internet
    </section>

    <p class="contact contact--phone">08-5550-1840</p>
    <p class="contact contact--web">brightlinecomputers.com.au</p>
  </main>
</body>
</html>
```